Homepage design for personal injury lawyer

NOTE: I will not close the project until June 9th. I want to give everyone time to put in their best work.
Your task is to redesign the homepage for this site:
https://corwistlane.com/
Feel free to use any images you find on the site.
I'm deliberately leaving the description simple so that I don't limit you.
Updates
Hi everyone. I will keep the project open for a few days to leave time for designs.
Number of Pages Required
1 page
Look and feel
Each slider illustrates characteristics of the customer's brand and the style your logo design should communicate.

```html
<!DOCTYPE html>
<html lang="en">
<head>
<meta charset="utf-8">
<title>Corwist Lane – Injury Lawyers</title>
<link href="https://fonts.googleapis.com/css2?family=Poppins:wght@400;500;600;700&family=Playfair+Display:ital,wght@1,700&display=swap" rel="stylesheet">
<style>
:root{
  --orange:#c4520f;
  --blue:#1565c0;
  --navy:#14213d;
  --ink:#111418;
  --text:#444a52;
  --muted:#6b7280;
  --pill:#e9eef7;
  --badge:#e6e6e6;
  --white:#ffffff;
}
*{margin:0;padding:0;box-sizing:border-box}
html,body{width:1200px;height:911px;overflow:hidden;background:var(--white)}
body{font-family:"Poppins",sans-serif;color:var(--ink);position:relative}
.abs{position:absolute}

.topbar{left:0;top:0;width:1200px;height:22px;background:var(--orange);color:#fff;font-size:8.5px}
.topbar .item{position:absolute;top:5px;display:flex;align-items:center;gap:5px}
.topbar svg{width:10px;height:10px}

.nav{left:0;top:22px;width:1200px;height:50px;background:var(--white)}
.brand{position:absolute;left:188px;top:9px;display:flex;align-items:center;gap:10px}
.brand .mark{width:36px;height:36px;border-radius:50%;background:#5f6368}
.brand .name{font-size:22px;font-weight:600;color:#5f6368;letter-spacing:.5px}
.menu{position:absolute;top:13px;left:600px;display:flex;align-items:center;font-size:9.5px;color:#333}
.menu a{color:inherit;text-decoration:none;padding:6px 10px;border-radius:4px}
.menu .active{background:var(--pill)}
.cta-small{position:absolute;left:935px;top:13px;width:93px;height:25px;background:var(--blue);color:#fff;font-size:8.5px;font-weight:600;border-radius:3px;display:flex;align-items:center;justify-content:center}

.hero{left:0;top:72px;width:1200px;height:572px}
.hero-photo{position:absolute;inset:0;background:
  linear-gradient(90deg,#f3f3f3 0%,#eeeeee 38%,#d9d3c8 55%,#8e7a63 68%,#2a3550 80%,#1e2a44 92%,#6f6250 100%)}
.badges{position:absolute;left:188px;top:68px;display:flex;gap:7px}
.badges span{display:block;height:29px;border-radius:3px;background:var(--badge)}
.headline{position:absolute;left:188px;top:110px;font-weight:700;font-size:53px;line-height:57px;letter-spacing:-.5px;color:var(--ink)}
.headline em{font-family:"Playfair Display",serif;font-style:italic;font-weight:700;color:var(--orange);letter-spacing:0}
.lede{position:absolute;left:188px;top:341px;width:400px;font-size:15px;line-height:23px;color:var(--text)}
.btn{position:absolute;top:406px;height:38px;border-radius:3px;font-size:12px;font-weight:600;display:flex;align-items:center;justify-content:center}
.btn-primary{left:188px;width:203px;background:var(--blue);color:#fff}
.btn-secondary{left:402px;width:189px;background:#fff;color:var(--ink)}
.stat{position:absolute;top:458px;display:flex;gap:8px}
.stat .num{font-size:20px;font-weight:600;line-height:24px;color:var(--navy)}
.stat .cap{font-size:7.5px;color:var(--muted);line-height:12px}
.stat svg{width:18px;height:18px;margin-top:14px}
.reviewer{font-size:18px;font-weight:500;color:#5f6368;margin-top:9px}

.media{left:0;top:644px;width:1200px;height:267px;background:var(--white)}
.media h2{position:absolute;top:50px;width:100%;text-align:center;font-size:10.5px;font-weight:600}
.outlets{position:absolute;top:96px;left:195px;width:805px;display:flex;justify-content:space-between;align-items:center}
.outlet{display:flex;align-items:center;gap:6px;font-size:13px;font-weight:600;color:#222}
.outlet i{display:block;width:14px;height:14px;border-radius:50%;background:#2b3a67}
</style>
</head>
<body>

<div class="abs topbar">
  <div class="item" style="left:774px">
    <svg viewBox="0 0 24 24" fill="none" stroke="#fff" stroke-width="2"><path d="M5 3h4l2 5-3 2a12 12 0 0 0 6 6l2-3 5 2v4a2 2 0 0 1-2 2A17 17 0 0 1 3 5a2 2 0 0 1 2-2z"/></svg>
    602-555-0148
  </div>
  <div class="item" style="left:868px">
    <svg viewBox="0 0 24 24" fill="none" stroke="#fff" stroke-width="2"><rect x="3" y="5" width="18" height="14" rx="2"/><path d="M3 7l9 6 9-6"/></svg>
    hello@corwistlane.com
  </div>
</div>

<header class="abs nav">
  <div class="brand"><span class="mark"></span><span class="name">Corwist Lane</span></div>
  <nav class="menu">
    <a class="active">Home</a>
    <a>What We Do &#8964;</a>
    <a>About</a>
    <a>Articles</a>
    <a>Contact Us</a>
  </nav>
  <div class="cta-small">Free Consultation</div>
</header>

<section class="abs hero">
  <div class="hero-photo" role="img" aria-label="Smiling attorney in navy suit, glasses and yellow tie, standing in a softly blurred office"></div>
  <div class="badges"><span style="width:101px"></span><span style="width:111px"></span><span style="width:115px"></span></div>
  <h1 class="headline">INJURY LAW<br><em>REDEFINED</em><br>WE WIN OR YOU<br>DON'T PAY</h1>
  <p class="lede">Over $100 million recovered for accident and injury victims. Available 24/7.</p>
  <div class="btn btn-primary">Srart Your Free Case Revies</div>
  <div class="btn btn-secondary">Call Now:&nbsp; 602-555-0193</div>

  <div class="stat" style="left:189px">
    <svg viewBox="0 0 24 24" fill="none" stroke="#c4520f" stroke-width="2"><path d="M12 3l8 3v6c0 5-4 8-8 9-4-1-8-4-8-9V6z"/></svg>
    <div><div class="num">99%</div><div class="cap">Won or Settled*</div></div>
  </div>
  <div class="stat" style="left:296px">
    <div class="reviewer">Reviewly</div>
    <div><div class="num">550 +</div><div class="cap">Over 550 5 Star Reviews</div></div>
  </div>
  <div class="stat" style="left:488px">
    <svg viewBox="0 0 24 24" fill="none" stroke="#c4520f" stroke-width="2"><rect x="3" y="5" width="18" height="13" rx="1"/><path d="M12 8v7M14 9.5h-3a1.5 1.5 0 0 0 0 3h2a1.5 1.5 0 0 1 0 3h-3M9 21h6"/></svg>
    <div><div class="num">0$</div><div class="cap">No fee unless you get<br>paid.</div></div>
  </div>
</section>

<section class="abs media">
  <h2>We are the legal experts the media calls</h2>
  <div class="outlets">
    <div class="outlet"><i></i>Vantage</div>
    <div class="outlet"><i></i>Orbit</div>
    <div class="outlet"><i></i>Harbor News</div>
    <div class="outlet"><i></i>Pulse</div>
    <div class="outlet"><i></i>Metro 24</div>
    <div class="outlet"><i></i>Daybreak</div>
    <div class="outlet"><i></i>Morning Hour</div>
    <div class="outlet"><i></i>Beacon</div>
    <div class="outlet">The Market Ledger</div>
  </div>
</section>

</body>
</html>
```